Inefficiency of Commercial Realestate (leasing, negotiation, etc)

I'm working on a powerpoint deck and I need some help making it more graphical. The powerpoint outlines the problems "problems" in the commercial real estate industry now and how our software makes the process easier. I'm trying to visualize the inefficiencies of brokers emailing back and forth a Microsoft word document then taking the negotiated document which is just a letter of intent and having to convert it into an abstract and a lease. When visualizing this conversion, I want to show that it's very tedious and prone to human error.
Problems to visualize:
Emailing a .doc file back and forth is frustrating and can take forever. Problems such as am I editing the right version, did they do it in a compatible version of word, etc
Once we've negotiated the LOI, manually converting it to a Lease and abstract takes time and is prone to human error. Additionally, if I want to hire a lawyer to do it it is expensive ($2-3k)
All this work is not reportable to my manager. If he wants to know what I've been spending my time on, I have to create an activity document and manually type it all out.
These documents are all over the place and not in one central location.
In addition to these visualizations, helping improve the overall look and feel and template of the attached presentation.

```html
<!DOCTYPE html>
<html lang="en">
<head>
<meta charset="utf-8">
<title>Leasio Deck – Market, Budget &amp; Plan</title>
<link href="https://fonts.googleapis.com/css2?family=Carlito:wght@400;700&display=swap" rel="stylesheet">
<style>
  :root {
    --blue: #0a73d9;
    --blue-dark: #0757b0;
    --blue-light: #3ea0f0;
    --ink: #1a1a1a;
    --link: #2a6fc9;
    --grid: #3c7fd6;
    --slide-top: #f4f5f7;
    --slide-bottom: #dcdfe4;
    --grey-box: #8e8e8e;
    --logo-grey: #8a8f96;
  }
  * { box-sizing: border-box; margin: 0; padding: 0; }
  html, body { width: 1200px; height: 724px; overflow: hidden; background: #fff; }
  body { position: relative; font-family: "Carlito", Calibri, Arial, sans-serif; color: var(--ink); }

  .slide {
    position: absolute; width: 380px; height: 288px;
    background: linear-gradient(180deg, var(--slide-top), var(--slide-bottom));
    box-shadow: 1px 2px 5px rgba(0,0,0,.35);
    overflow: hidden;
  }
  .slide-title {
    height: 42px; padding: 11px 10px 0;
    background: linear-gradient(90deg, var(--blue) 0%, var(--blue-light) 75%, #e6eefa 100%);
    color: #fff; font-size: 16px; font-weight: 400;
  }
  .footer { position: absolute; left: 0; right: 0; bottom: 6px; height: 16px; font-size: 6px; color: var(--blue); }
  .footer .page { position: absolute; left: 12px; top: 4px; }
  .footer .conf { position: absolute; left: 0; right: 0; top: 4px; text-align: center; }
  .brand { position: absolute; right: 8px; top: 0; display: flex; align-items: center; gap: 3px; }
  .brand-name { font-size: 13px; font-weight: 700; color: var(--logo-grey); letter-spacing: .5px; }
  .brand-tag { font-size: 4px; color: var(--logo-grey); width: 34px; line-height: 1.1; }

  table { border-collapse: collapse; table-layout: fixed; }

  /* slide 1 */
  .market-table { position: absolute; left: 14px; top: 52px; width: 350px; }
  .market-table td { border: 1px solid var(--grid); font-size: 8.5px; text-align: center; height: 61px; padding: 0 3px; line-height: 1.3; }
  .note { position: absolute; right: 12px; top: 243px; font-size: 6px; }

  /* slide 2 */
  .partner-band { position: absolute; left: 0; top: 42px; width: 380px; height: 82px; background: #fdfdfd; }
  .partner { position: absolute; display: flex; align-items: center; gap: 4px; font-size: 12px; font-weight: 700; }
  .partner .mark { width: 10px; height: 10px; }
  .segment { position: absolute; left: 13px; width: 349px; height: 32px; display: flex; }
  .segment-label { width: 128px; background: var(--blue); color: #fff; font-size: 9px; display: flex; align-items: center; justify-content: center; }
  .segment table { width: 221px; height: 32px; background: #fff; }
  .segment td { border: 1px solid var(--grid); font-size: 9px; text-align: center; }
  .segment td:first-child { width: 119px; }

  /* slide 3 */
  .budget-table { position: absolute; left: 36px; top: 54px; width: 292px; }
  .budget-table td { border: 1px solid var(--grid); font-size: 9.5px; height: 15.8px; padding: 0 2px; }
  .budget-table td:last-child { text-align: right; width: 92px; }
  .legal-bar { position: absolute; left: 36px; top: 241px; width: 292px; height: 20px; background: var(--blue); color: #fff; font-size: 9px; display: flex; align-items: center; justify-content: center; box-shadow: 0 1px 2px rgba(0,0,0,.3); }

  /* slide 4 */
  .fin-table { position: absolute; left: 12px; top: 54px; width: 356px; }
  .fin-table td { border: 1px solid var(--grid); font-size: 9.5px; height: 16.6px; text-align: center; }
  .fin-table td.label { text-align: left; padding-left: 2px; color: var(--link); width: 94px; }
  .fin-table tr.band td.label, .fin-table td.hd { background: var(--blue); color: #fff; }
  .fin-table tr.years td { color: var(--link); }
  .fin-table tr.band td { height: 18px; }

  /* slide 5 */
  .rev-label { position: absolute; top: 87px; height: 28px; background: var(--grey-box); color: #fff; font-size: 10px; display: flex; align-items: center; justify-content: center; text-align: center; line-height: 1.1; box-shadow: 1px 1px 2px rgba(0,0,0,.35); }
  .rev-icon { position: absolute; top: 141px; width: 60px; height: 60px; }

  /* slide 6 */
  .phase { position: absolute; top: 83px; width: 104px; height: 46px; }
  .phase-note { position: absolute; top: 149px; width: 102px; height: 69px; background: #f7f7f7; border: 1px solid #b9b9b9; box-shadow: 1px 1px 2px rgba(0,0,0,.25); font-size: 8px; line-height: 1.35; padding: 3px; }
  .connector { position: absolute; top: 129px; width: 1px; height: 20px; background: var(--blue-dark); }
  .connector::after { content: ""; position: absolute; left: -2px; top: 2px; width: 5px; height: 5px; border-radius: 50%; background: var(--blue-dark); }
</style>
</head>
<body>

<section class="slide" style="left:10px; top:48px;">
  <h2 class="slide-title">U.S. Market Opportunity</h2>
  <table class="market-table">
    <tr><td style="width:85px"></td><td style="width:82px"># brokers (USA)</td><td style="width:91px">average cost / month</td><td>Revenue Opportunity / year</td></tr>
    <tr><td></td><td>466,100</td><td>$75.00</td><td>$419,490,000.00</td></tr>
    <tr><td></td><td></td><td></td><td>10% of market penetration<br>~$42MM/year</td></tr>
  </table>
  <p class="note">* does not account for added value of reporting industry data</p>
  <div class="footer"><span class="page">8</span><span class="conf">Confidential</span>
    <span class="brand"><span class="brand-name">LEASIO</span><span class="brand-tag">Smarter lease documentation</span></span></div>
</section>

<section class="slide" style="left:405px; top:48px;">
  <h2 class="slide-title">Local Market Opportunities</h2>
  <div class="partner-band">
    <div class="partner" style="left:34px; top:14px; color:#1d6b3b;">Northgate Realty</div>
    <div class="partner" style="left:226px; top:14px; color:#222;"><span class="mark" style="background:#d9262b"></span>Harlow &amp; Pierce</div>
    <div class="partner" style="left:34px; top:48px; color:#8a8a8a; font-weight:400;"><span class="mark" style="background:#9a9a9a"></span>Brightwell Partners</div>
    <div class="partner" style="left:226px; top:48px; color:#1b2f6e;"><span class="mark" style="background:#1b2f6e"></span>Summit Ridge Realty</div>
  </div>
  <div class="segment" style="top:137px"><div class="segment-label">Industrial Market</div>
    <table><tr><td>users</td><td>$50/user/month</td></tr><tr><td>100</td><td>$5,000</td></tr></table></div>
  <div class="segment" style="top:180px"><div class="segment-label">Office Market</div>
    <table><tr><td>users</td><td>$100/user/month</td></tr><tr><td>75</td><td>$7,500</td></tr></table></div>
  <div class="segment" style="top:220px"><div class="segment-label">Retail Market</div>
    <table><tr><td>users</td><td>$100/user/month</td></tr><tr><td>75</td><td>$7,500</td></tr></table></div>
  <div class="footer"><span class="page">9</span><span class="conf">Confidential</span>
    <span class="brand"><span class="brand-name">LEASIO</span><span class="brand-tag">Smarter lease documentation</span></span></div>
</section>

<section class="slide" style="left:802px; top:48px;">
  <h2 class="slide-title">1 Year Budget</h2>
  <table class="budget-table">
    <tr><td>CEO</td><td>$100,000</td></tr>
    <tr><td>Developers (2)</td><td>$80,000</td></tr>
    <tr><td>Rent</td><td>$24,000</td></tr>
    <tr><td>Hosting</td><td>$10,000</td></tr>
    <tr><td>Design</td><td>$10,000</td></tr>
    <tr><td>Accounting</td><td>$5,000</td></tr>
    <tr><td>Marketing/Advertising</td><td>$20,000</td></tr>
    <tr><td>Computers</td><td>$5,000</td></tr>
    <tr><td></td><td></td></tr>
    <tr><td>unplanned expenses</td><td>$20,000</td></tr>
    <tr><td>total</td><td>$274,000</td></tr>
  </table>
  <div class="legal-bar">Legal Language for industrial,&nbsp; retail,&nbsp; office&nbsp;&nbsp;&nbsp;$50,000</div>
  <div class="footer"><span class="page">10</span><span class="conf">Confidential</span>
    <span class="brand"><span class="brand-name">LEASIO</span><span class="brand-tag">Smarter lease documentation</span></span></div>
</section>

<section class="slide" style="left:10px; top:387px;">
  <h2 class="slide-title">5 year financial</h2>
  <table class="fin-table">
    <tr><td class="label"></td><td class="hd" colspan="5">users</td></tr>
    <tr class="years"><td class="label"></td><td>y1</td><td>y2</td><td>y3</td><td>y4</td><td>y5</td></tr>
    <tr><td class="label">Market Industrial</td><td>10</td><td>100</td><td>200</td><td>500</td><td>1,000</td></tr>
    <tr><td class="label">Market Office</td><td>5</td><td>100</td><td>200</td><td>500</td><td>1,000</td></tr>
    <tr><td class="label">Market Retail</td><td>5</td><td>100</td><td>200</td><td>500</td><td>1,000</td></tr>
    <tr><td class="label"></td><td></td><td></td><td></td><td></td><td></td></tr>
    <tr><td class="label"></td><td></td><td></td><td></td><td></td><td></td></tr>
    <tr class="band"><td class="label">Revenue</td><td>$18,000</td><td>$300,000</td><td>$600,000</td><td>$1,500,000</td><td>$3,000,000</td></tr>
    <tr><td class="label"></td><td></td><td></td><td></td><td></td><td></td></tr>
    <tr class="band"><td class="label">Expenses</td><td>$247,000</td><td>$247,000</td><td>$247,000</td><td>$247,000</td><td>$247,000</td></tr>
    <tr><td class="label"></td><td></td><td></td><td></td><td></td><td></td></tr>
    <tr class="band"><td class="label">Net</td><td>-$229,000</td><td>$53,000</td><td>$353,000</td><td>$1,253,000</td><td>$2,753,000</td></tr>
  </table>
  <div class="footer"><span class="page">11</span><span class="conf">Confidential</span>
    <span class="brand"><span class="brand-name">LEASIO</span><span class="brand-tag">Smarter lease documentation</span></span></div>
</section>

<section class="slide" style="left:405px; top:387px;">
  <h2 class="slide-title">Additional Revenue</h2>
  <div class="rev-label" style="left:5px; width:123px;">Industry Analytics and<br>Statistical Information</div>
  <div class="rev-label" style="left:141px; width:95px;">Mortgage Industry</div>
  <div class="rev-label" style="left:257px; width:120px;">Commercial Lending</div>
  <svg class="rev-icon" style="left:30px" viewBox="0 0 60 60" role="img" aria-label="Analytics chart icon">
    <circle cx="30" cy="30" r="29" fill="var(--blue)"/>
    <g fill="#fff"><rect x="16" y="34" width="5" height="10"/><rect x="24" y="29" width="5" height="15"/><rect x="32" y="31" width="5" height="13"/><rect x="40" y="24" width="5" height="20"/></g>
    <polyline points="15,30 25,22 33,26 44,15" fill="none" stroke="#fff" stroke-width="2"/>
    <polygon points="40,14 46,13 45,19" fill="#fff"/>
  </svg>
  <svg class="rev-icon" style="left:159px" viewBox="0 0 60 60" role="img" aria-label="House icon">
    <circle cx="30" cy="30" r="29" fill="var(--blue)"/>
    <path d="M30 13 L47 29 H42 V45 H18 V29 H13 Z" fill="#fff"/>
    <rect x="26" y="34" width="8" height="11" fill="var(--blue)"/>
  </svg>
  <svg class="rev-icon" style="left:286px" viewBox="0 0 60 60" role="img" aria-label="Money bag icon">
    <circle cx="30" cy="30" r="29" fill="var(--blue)"/>
    <path d="M24 16 H34 L31 22 C40 26 43 34 41 41 C40 45 35 46 29 46 C22 46 17 45 17 40 C16 33 20 26 27 22 Z" fill="#fff"/>
    <text x="29" y="39" font-size="12" font-weight="700" fill="var(--blue)" text-anchor="middle" font-family="Carlito, sans-serif">$</text>
    <g fill="#fff"><rect x="39" y="42" width="9" height="3" rx="1"/><rect x="39" y="38" width="9" height="3" rx="1"/><rect x="39" y="34" width="9" height="3" rx="1"/></g>
  </svg>
  <div class="footer"><span class="page">12</span><span class="conf">Confidential</span>
    <span class="brand"><span class="brand-name">LEASIO</span><span class="brand-tag">Smarter lease documentation</span></span></div>
</section>

<section class="slide" style="left:802px; top:387px;">
  <h2 class="slide-title">Business Plan</h2>
  <svg class="phase" style="left:18px" viewBox="0 0 104 46"><polygon points="0,0 90,0 104,23 90,46 0,46 12,23" fill="var(--blue)"/><text x="52" y="27" fill="#fff" font-size="11.5" text-anchor="middle" font-family="Carlito, sans-serif">3 months</text></svg>
  <svg class="phase" style="left:140px" viewBox="0 0 104 46"><polygon points="0,0 90,0 104,23 90,46 0,46 12,23" fill="var(--blue)"/><text x="52" y="27" fill="#fff" font-size="11.5" text-anchor="middle" font-family="Carlito, sans-serif">6 months</text></svg>
  <svg class="phase" style="left:260px" viewBox="0 0 104 46"><polygon points="0,0 90,0 104,23 90,46 0,46 12,23" fill="var(--blue)"/><text x="52" y="27" fill="#fff" font-size="11.5" text-anchor="middle" font-family="Carlito, sans-serif">Ongoing</text></svg>
  <span class="connector" style="left:63px"></span>
  <span class="connector" style="left:192px"></span>
  <span class="connector" style="left:311px"></span>
  <div class="phase-note" style="left:20px">launch industrial.leasio.co, office.leasio.co and retail.leasio.co</div>
  <div class="phase-note" style="left:142px">Market towards larger institutions for specific sectors of their business (Brightwell Partners, Dale Morrow, etc)</div>
  <div class="phase-note" style="left:262px">Identify and foster other verticals (Commercial Lending, Mortgages, Insurance)</div>
  <div class="footer"><span class="page">13</span><span class="conf">Confidential</span>
    <span class="brand"><span class="brand-name">LEASIO</span><span class="brand-tag">Smarter lease documentation</span></span></div>
</section>

</body>
</html>
```